Ferlande Glues

Website for funeral directors see the original website: http://pates-ferlande.be
Target Market(s)
B2C
Coding
Coded - Design and coding required
Number of Pages Required
5+ page
Font styles to use
Serif
Sans Serif
Script
Colors
9d9d9d
757575
e667a6
eea4c8
e34197
Requirements
Must have
- Keep the architecture of the current site.
Nice to have
- A page with a list of people who have died. See example: https://www.maisonbrevant.be

```html
<!DOCTYPE html>
<html lang="en">
<head>
<meta charset="utf-8">
<title>Ferlande Glues – Funeral Home</title>
<link rel="stylesheet" href="https://fonts.googleapis.com/css2?family=Roboto:ital,wght@0,400;0,500;0,700;1,500&family=Open+Sans:ital,wght@0,400;0,600;1,400&display=swap">
<style>
:root{
  --pink:#e34197;
  --pink-mid:#e667a6;
  --pink-light:#eea4c8;
  --grey:#8d8d8d;
  --grey-card:#6d6d6d;
  --grey-text:#757575;
  --grey-light:#9d9d9d;
  --dark:#222;
  --white:#fff;
  --green:#1f6b3a;
}
*{margin:0;padding:0;box-sizing:border-box}
html,body{width:1200px;height:3815px;overflow:hidden}
body{position:relative;background:var(--white);font-family:"Open Sans",Arial,sans-serif;color:var(--grey-text)}
.abs{position:absolute}
.center{text-align:center}

/* hero */
.hero{left:0;top:0;width:1200px;height:662px;background:linear-gradient(180deg,#5a564f 0%,#7c776e 35%,#3a3a3c 60%,#6d6a64 85%,#8a857c 100%)}
.hero-photo{position:absolute;inset:0}
.brand{left:111px;top:30px;width:234px;height:170px;display:flex;align-items:center;justify-content:center;gap:12px}
.brand-dot{width:14px;height:14px;border-radius:50%;background:var(--pink)}
.brand-name{font-family:"Roboto",sans-serif;font-weight:500;font-size:26px;color:var(--white)}
.nav{right:112px;top:76px;display:flex;gap:20px;font-family:"Roboto",sans-serif;font-size:15px;color:var(--white)}
.nav .active{color:var(--pink)}
.hero-quote{left:0;top:240px;width:1200px;font-family:"Roboto",sans-serif;font-style:italic;font-weight:500;font-size:36px;line-height:52px;color:var(--white);text-shadow:0 2px 4px rgba(0,0,0,.4)}
.dots{left:566px;top:585px;display:flex;gap:6px}
.dots span{width:13px;height:13px;border-radius:50%;border:2px solid var(--white)}
.dots span.on{background:var(--white)}

/* welcome */
.welcome-title{left:0;top:752px;width:1200px;font-family:"Roboto",sans-serif;font-size:46px;font-weight:500;color:var(--dark)}
.welcome-text{left:250px;top:836px;width:700px;font-size:15px;line-height:29px}
.welcome-text p+p{margin-top:29px}
.feature{top:1067px;width:313px}
.feature-img{width:313px;height:230px;border-radius:3px}
.feature h3{margin-top:32px;font-family:"Roboto",sans-serif;font-weight:500;font-size:21px;line-height:30px;color:var(--dark)}
.feature .bar{margin-top:12px;width:104px;height:4px;background:var(--pink)}
.feature p{margin-top:26px;font-size:15px;line-height:29px}
.feature .more{display:block;margin-top:16px;font-family:"Roboto",sans-serif;font-weight:700;font-size:15px;color:var(--pink)}

/* deaths */
.deaths{left:0;top:1637px;width:1200px;height:1370px;background:var(--grey)}
.deaths-title{left:0;top:1718px;width:1200px;font-family:"Roboto",sans-serif;font-size:46px;font-weight:500;color:var(--white)}
.person{width:296px;height:434px;background:var(--grey-card);color:var(--white);text-align:center}
.person h4{margin-top:26px;font-family:"Roboto",sans-serif;font-weight:500;font-size:21px}
.person .home{margin-top:2px;font-family:"Roboto",sans-serif;font-size:15px;color:#e6e6e6}
.person .photo{margin:14px auto 0;width:216px;height:218px}
.person .date{margin-top:12px;font-size:14px}
.person .btn{display:inline-block;margin-top:10px;width:128px;height:44px;line-height:44px;border-radius:22px;background:var(--white);color:var(--pink);font-family:"Roboto",sans-serif;font-weight:700;font-size:16px}
.view-more{left:524px;top:2796px;width:153px;height:50px;line-height:46px;border:2px solid var(--white);border-radius:25px;color:var(--white);font-family:"Roboto",sans-serif;font-weight:700;font-size:16px;text-align:center}

/* testimonials */
.testi-band{left:0;top:2874px;width:1200px;height:489px;background:linear-gradient(180deg,#e34197 0%,#dc3d91 50%,#e34197 100%)}
.testi-cut{left:0;top:2873px}
.testi-title{left:0;top:3078px;width:1200px;font-family:"Roboto",sans-serif;font-size:46px;font-weight:500;color:var(--white)}
.quote-card{top:3207px;width:308px;height:260px;background:var(--white);box-shadow:0 2px 6px rgba(0,0,0,.18);text-align:center;padding:0 14px}
.avatar{position:absolute;left:108px;top:-46px;width:92px;height:92px;border-radius:50%;border:3px solid var(--white);box-shadow:0 0 0 1px #ccc;background:linear-gradient(160deg,#e9e6e3,#b9a99c)}
.quote-card blockquote{margin-top:68px;height:112px;overflow:hidden;font-style:italic;font-size:12.5px;line-height:25px;color:#777}
.quote-card .who{margin-top:4px;font-family:"Roboto",sans-serif;font-size:20px;line-height:26px;color:var(--dark)}
.quote-card .role{margin-top:6px;font-style:italic;font-size:14px;color:var(--green)}
.arrow{top:3284px;width:44px;height:44px}

/* footer */
.social{left:487px;top:3565px;display:flex;gap:9px}
.social span{width:50px;height:50px;border-radius:50%;border:1.5px solid #999;display:block}
.contact{left:0;top:3651px;width:1200px;font-size:15px;color:#555;display:flex;justify-content:center;align-items:center;gap:8px}
.contact svg{flex:none}
.links{left:0;top:3699px;width:1200px;font-size:14px;color:#555;text-align:center;word-spacing:2px}
.copy{left:0;top:3740px;width:1200px;font-size:14px;color:#555;text-align:center}
</style>
</head>
<body>

<header>
  <div class="abs hero"><div class="hero-photo" role="img" aria-label="Black hearse parked in front of a stone church"></div></div>
  <div class="abs brand"><span class="brand-dot"></span><span class="brand-name">Ferlande Glues</span></div>
  <nav class="abs nav">
    <span class="active">Home</span><span>Our society</span><span>What to do in case of death?</span><span>Our services</span><span>They have left us</span><span>Contact</span>
  </nav>
  <p class="abs hero-quote center">The tree owes the beauty of its fruits to the strength<br>of its bark and the wisdom of its roots ...</p>
  <div class="abs dots"><span class="on"></span><span></span><span></span><span></span></div>
</header>

<main>
  <h1 class="abs welcome-title center">Welcome to Ferlande Glues</h1>
  <div class="abs welcome-text center">
    <p>Founded in 1898 by Emile FERLANDE, the family funeral home FERLANDE GLUES's sole concern is to relieve the pain and sadness you endure when losing a loved one.</p>
    <p>Whatever your origins, your beliefs or your traditions, we support you and offer a complete range of services and products adapted to your needs. We organize the funeral and take care of the various administrative procedures related to the death.</p>
  </div>

  <article class="abs feature" style="left:111px">
    <div class="feature-img" role="img" aria-label="Funeral home reception hall" style="background:linear-gradient(135deg,#d8d6d2,#6b5f4e 60%,#9a8f7d)"></div>
    <h3>Complete Funeral<br>Organization</h3><div class="bar"></div>
    <p>Our first concern is to simplify the decision making made very difficult in a moment ...</p>
    <span class="more">READ MORE</span>
  </article>
  <article class="abs feature" style="left:443px">
    <div class="feature-img" role="img" aria-label="Smiling elderly couple in sunlight" style="background:linear-gradient(135deg,#f4d6a0,#c99a6a 55%,#8c8a4f)"></div>
    <h3>Plan Your Funeral In<br>Advance</h3><div class="bar"></div>
    <p>By organizing your funeral in advance, you freely decide in detail how your funeral...</p>
    <span class="more">READ MORE</span>
  </article>
  <article class="abs feature" style="left:775px">
    <div class="feature-img" role="img" aria-label="Funeral home shop front with flower display" style="background:linear-gradient(135deg,#b9bcc3,#555a66 55%,#9ea1a6)"></div>
    <h3>Have Your Flowers<br>Delivered Online</h3><div class="bar"></div>
    <p>Order your natural flowers and silk flowers directly through our website,..</p>
    <span class="more">READ MORE</span>
  </article>

  <section>
    <div class="abs deaths"></div>
    <h2 class="abs deaths-title center">Latest Deaths</h2>

    <div class="abs person" style="left:111px;top:1828px"><h4>Marc VERHOEVEN</h4><div class="home">Brevant Funeral Homes</div><div class="photo" role="img" aria-label="Portrait of the deceased" style="background:linear-gradient(180deg,#fff 30%,#b9c9dc)"></div><div class="date">on 06 June 2019</div><span class="btn">FUNERALS</span></div>
    <div class="abs person" style="left:452px;top:1828px"><h4>Adams Paul</h4><div class="home">Brevant Funeral Homes</div><div class="photo" role="img" aria-label="Portrait of the deceased" style="background:linear-gradient(180deg,#fff 30%,#c8b9a0)"></div><div class="date">on 06 June 2019</div><span class="btn">FUNERALS</span></div>
    <div class="abs person" style="left:793px;top:1828px"><h4>Robert</h4><div class="home">Brevant Funeral Homes</div><div class="photo" role="img" aria-label="Portrait of the deceased" style="background:linear-gradient(180deg,#fff 30%,#bdbdbd)"></div><div class="date">on 06 June 2019</div><span class="btn">FUNERALS</span></div>

    <div class="abs person" style="left:111px;top:2308px"><h4>Lucy VERHOEVEN</h4><div class="home">Brevant Funeral Homes</div><div class="photo" role="img" aria-label="Portrait of the deceased" style="background:linear-gradient(180deg,#fff 30%,#e2cde6)"></div><div class="date">on 06 June 2019</div><span class="btn">FUNERALS</span></div>
    <div class="abs person" style="left:452px;top:2308px"><h4>Henry</h4><div class="home">Brevant Funeral Homes</div><div class="photo" role="img" aria-label="Portrait of the deceased" style="background:linear-gradient(180deg,#fff 30%,#aeb6c2)"></div><div class="date">on 06 June 2019</div><span class="btn">FUNERALS</span></div>
    <div class="abs person" style="left:793px;top:2308px"><h4>Pascale MOREAU</h4><div class="home">Brevant Funeral Homes</div><div class="photo" role="img" aria-label="Portrait of the deceased" style="background:linear-gradient(180deg,#fff 30%,#c4c4c4)"></div><div class="date">on 06 June 2019</div><span class="btn">FUNERALS</span></div>

    <span class="abs view-more">VIEW MORE</span>
  </section>

  <section>
    <div class="abs testi-band" role="img" aria-label="Funeral home building tinted in pink"></div>
    <svg class="abs testi-cut" width="1200" height="136" viewBox="0 0 1200 136"><polygon points="0,0 1200,0 1200,8 822,134 0,1" fill="#8d8d8d"/></svg>
    <h2 class="abs testi-title center">Client Testimonials</h2>

    <svg class="abs arrow" style="left:22px" viewBox="0 0 44 44"><circle cx="22" cy="22" r="20.5" fill="none" stroke="#fff" stroke-width="1.5"/><polyline points="25,14 17,22 25,30" fill="none" stroke="#fff" stroke-width="2"/></svg>
    <svg class="abs arrow" style="left:1132px" viewBox="0 0 44 44"><circle cx="22" cy="22" r="20.5" fill="none" stroke="#fff" stroke-width="1.5"/><polyline points="19,14 27,22 19,30" fill="none" stroke="#fff" stroke-width="2"/></svg>

    <div class="abs quote-card" style="left:98px"><div class="avatar" role="img" aria-label="Client portrait"></div><blockquote>In the emotional aftermath of the first hours of your death, the most positive thing about your service is the welcome by telephone and the services provided by your staff.</blockquote><div class="who">Bertrand Lemaire</div><div class="role">Propriétaire - Lemaire Média</div></div>
    <div class="abs quote-card" style="left:446px"><div class="avatar" role="img" aria-label="Client portrait"></div><blockquote>Good staff presentation, respect and discretion, the explanation of the care given to the deceased person was very complete. The administrative formalities file</blockquote><div class="who">André Varlet</div><div class="role">Propriétaire - Azur Voyages</div></div>
    <div class="abs quote-card" style="left:794px"><div class="avatar" role="img" aria-label="Client portrait"></div><blockquote>We hereby warmly thank you for your efficiency and your valuable collaboration.</blockquote><div class="who">Jacques Helmer</div><div class="role">Propriétaire - Moment Rare</div></div>
  </section>
</main>

<footer>
  <div class="abs social" aria-label="Social networks"><span></span><span></span><span></span><span></span></div>
  <div class="abs contact">
    <svg width="12" height="16" viewBox="0 0 12 16"><path d="M6 0C2.7 0 0 2.6 0 5.8 0 10 6 16 6 16s6-6 6-10.2C12 2.6 9.3 0 6 0zm0 8.2A2.4 2.4 0 1 1 6 3.4a2.4 2.4 0 0 1 0 4.8z" fill="#e34197"/></svg>
    <span>rue des Tilleuls 48 6700 ARLON</span><span>|</span>
    <svg width="14" height="14" viewBox="0 0 14 14"><path d="M3 0l2.4 3.2-1.5 1.7c.8 1.9 2.3 3.4 4.2 4.2l1.7-1.5L13 10l-1.3 2.8C6 13 1 8 1.2 2.3z" fill="#e34197"/></svg>
    <span>+32 (0) 63 / 40.17.83</span><span>|</span>
    <svg width="17" height="13" viewBox="0 0 17 13"><rect width="17" height="13" rx="1.5" fill="#e34197"/><polyline points="1,1.5 8.5,7.5 16,1.5" fill="none" stroke="#fff" stroke-width="1.4"/></svg>
    <span>arlon@ferlande-glues.be</span>
  </div>
  <div class="abs links">Help &nbsp; | &nbsp; FAQ &nbsp; | &nbsp; Support &nbsp; | &nbsp; Sitemap &nbsp; | &nbsp; Terms Of Use &nbsp; | &nbsp; Privacy Statement</div>
  <div class="abs copy">Ferlande Glues © 2019 All rights reserved.</div>
</footer>

</body>
</html>
```